New Crowdfunding site Fundlark needs banner ads

I’m looking for 4 standard size banner ads for www.fundlark.example to be used by TradeQuill Affiliates in order to bring new crowdfunding projects to the platform.
728x90
160x600
300x250
180x160

Succesful designers will put on our Mentors list so that the project owner can also get their specific project banners from our designers. Designers can also become our affiliates either to promote Fundlark.example or individual projects.
Updates

Please note updated brief

Thank you to those that have submitted designs so far.
Please be reminded that the invitation will close tomorrow after which we will make our choice

Thanks for input so far.
Please note project closes tomorrow (Sunday) after which we will choose.

Target Market(s)

Target is a project owner with a project requiring $10,000 or more in any field including business and/or non-profits. Any country.
Inventors, creatives, communities, hardware or software, consumer items,

Industry/Entity Type

Crowdfunding

Font styles to use
Sans Serif

Requirements
Must have
• Clear button call to action based on our USPs shown on the home page but especially the use of Affiliate Networks to promote their project to the widest possible audience.

Text and button text should be editable (see png preference).
Call to action could be based on "Free Crowdfunding Consultation - is your project viable" or "Get Your Free Guide to Succesful Crowdfunding"
Nice to have
• .png format preferred with separate objects.
Some animation preferred in the button.

```html
<!DOCTYPE html>
<html lang="en">
<head>
<meta charset="utf-8">
<title>Fundlark banner set</title>
<link rel="stylesheet" href="https://fonts.googleapis.com/css2?family=Open+Sans:wght@400;600&display=swap">
<style>
  :root {
    --sheet-light: #ececec;
    --sheet-mid: #d9d9d9;
    --label: #1e1e1e;
    --brand-blue: #1f4f7a;
    --ink: #1a1a1a;
    --white: #ffffff;
    --paper-grey: #efefef;
    --sky-top: #3f7fd0;
    --sky-mid: #4a89d8;
    --sky-low: #243f7c;
    --navy-deep: #101a5a;
    --navy-mid: #2a2f8f;
    --violet: #5b3aa8;
    --violet-glow: #8a55c0;
    --plum-deep: #5a1455;
    --plum-mid: #8a2a7e;
    --plum-glow: #b0529f;
    --accent-pink: #e648e2;
    --cta-top: #ffd22e;
    --cta-bottom: #f79a16;
    --cta-arrow: #f5a31a;
    --night: #0b0b12;
  }
  * { box-sizing: border-box; margin: 0; padding: 0; }
  html, body { width: 1200px; height: 900px; overflow: hidden; }
  body {
    position: relative;
    font-family: "Open Sans", Arial, sans-serif;
    color: var(--ink);
  }
  .sheet-backdrop {
    position: absolute; inset: 0;
    background: radial-gradient(ellipse at 50% 40%, var(--sheet-light), var(--sheet-mid));
  }
  .size-label {
    position: absolute;
    font-size: 28px; line-height: 1;
    color: var(--label);
    transform: translateX(-50%);
    white-space: nowrap;
  }
  .banner { position: absolute; overflow: hidden; }
  .banner-art { position: absolute; inset: 0; }
  .t {
    position: absolute; line-height: 1; white-space: nowrap;
    color: var(--white);
  }
  .t-center { left: 0; right: 0; text-align: center; }
  .headline { text-shadow: 0 2px 4px rgba(0,0,0,.55); }
  .accent { color: var(--accent-pink); }

  .brand-name { color: var(--brand-blue); font-weight: 400; }
  .brand-line { color: var(--ink); }
  .brand-dot {
    position: absolute; border-radius: 50%;
    background: var(--brand-blue);
  }

  .cta {
    position: absolute;
    display: flex; align-items: center; justify-content: space-between;
    padding: 0 9px 0 12px;
    border-radius: 6px;
    background: linear-gradient(var(--cta-top), var(--cta-bottom));
    box-shadow: 0 2px 3px rgba(0,0,0,.35);
    color: var(--ink); font-size: 14px; line-height: 1;
  }
  .cta svg { width: 18px; height: 18px; flex: none; }

  /* leaderboard 728 x 90 */
  .leaderboard { width: 728px; height: 90px; left: 17px; }
  .leaderboard .brand-panel { position: absolute; left: 0; top: 0; width: 206px; height: 90px; }
  .leaderboard .cta { left: 602px; top: 40px; width: 117px; height: 34px; }

  /* medium rectangle 300 x 250 */
  .rectangle { width: 300px; height: 250px; top: 391px; }
  .rectangle .cta { left: 94px; top: 209px; width: 119px; height: 33px; }

  /* skyscraper 160 x 600 */
  .skyscraper { width: 160px; height: 600px; top: 42px; }
  .skyscraper .cta { left: 7px; top: 549px; width: 143px; height: 39px; padding-left: 11px; }
  .skyscraper .base-band { position: absolute; left: 0; right: 0; top: 584px; height: 16px; background: var(--night); }

  /* small square 180 x 160 */
  .square { width: 180px; height: 160px; }
  .square .cta { left: 23px; top: 124px; width: 126px; height: 31px; }
</style>
</head>
<body>
  <div class="sheet-backdrop" role="img" aria-label="Soft grey faceted presentation background"></div>

  <div class="size-label" style="left:982px; top:9px;">160 x 600</div>
  <div class="size-label" style="left:400px; top:155px;">728 x 90</div>
  <div class="size-label" style="left:388px; top:328px;">300 x 250</div>
  <div class="size-label" style="left:769px; top:663px;">180 x 160</div>

  <!-- Leaderboard: free guide -->
  <section class="banner leaderboard" style="top:45px;">
    <div class="banner-art" role="img" aria-label="Blue sky gradient backdrop"
         style="background:linear-gradient(var(--sky-top) 0%, var(--sky-mid) 55%, var(--sky-low) 100%);"></div>
    <svg class="brand-panel" viewBox="0 0 206 90" aria-hidden="true">
      <polygon fill="#ffffff" points="0,0 198,0 206,6 198,12 206,18 198,24 206,30 198,36 206,42 198,48 206,54 198,60 206,66 198,72 206,78 198,84 206,90 0,90"/>
    </svg>
    <span class="brand-dot" style="left:5px; top:25px; width:40px; height:40px;"></span>
    <span class="t brand-name" style="left:53px; top:27px; font-size:25px;">Fundlark</span>
    <span class="t brand-line" style="left:54px; top:56px; font-size:12px;">Project +&nbsp; Crowdfunding</span>
    <span class="t" style="left:230px; top:16px; font-size:17px;">GET YOUR FREE GUIDE TO</span>
    <span class="t" style="left:249px; top:37px; font-size:21px;">SUCCESSFUL CROWDFUNDING</span>
    <a class="cta">Learn More <svg viewBox="0 0 18 18"><circle cx="9" cy="9" r="9" fill="#fff"/><polygon points="7,5 13,9 7,13" fill="var(--cta-arrow)"/></svg></a>
  </section>

  <!-- Leaderboard: consultation -->
  <section class="banner leaderboard" style="top:207px;">
    <div class="banner-art" role="img" aria-label="Deep navy and violet faceted backdrop"
         style="background:linear-gradient(100deg, var(--navy-deep) 20%, var(--navy-mid) 55%, var(--violet-glow) 100%);"></div>
    <svg class="brand-panel" viewBox="0 0 206 90" aria-hidden="true">
      <polygon fill="#efefef" points="0,0 198,0 206,6 198,12 206,18 198,24 206,30 198,36 206,42 198,48 206,54 198,60 206,66 198,72 206,78 198,84 206,90 0,90"/>
    </svg>
    <span class="brand-dot" style="left:5px; top:25px; width:40px; height:40px;"></span>
    <span class="t brand-name" style="left:53px; top:27px; font-size:25px;">Fundlark</span>
    <span class="t brand-line" style="left:54px; top:56px; font-size:12px;">Project +&nbsp; Crowdfunding</span>
    <span class="t" style="left:223px; top:22px; font-size:17px;">FREE CROWDFUNDING CONSULTATION</span>
    <span class="t" style="left:424px; top:51px; font-size:13px;">IS YOUR PROJECT VIBLE</span>
    <a class="cta">Learn More <svg viewBox="0 0 18 18"><circle cx="9" cy="9" r="9" fill="#fff"/><polygon points="7,5 13,9 7,13" fill="var(--cta-arrow)"/></svg></a>
  </section>

  <!-- Rectangles -->
  <section class="banner rectangle" style="left:18px;">
    <div class="banner-art" role="img" aria-label="Deep navy and violet faceted backdrop"
         style="background:linear-gradient(135deg, var(--navy-deep) 10%, var(--navy-mid) 50%, var(--violet-glow) 100%);"></div>
    <svg class="banner-art" viewBox="0 0 300 250" aria-hidden="true"><path d="M0 0H300V40Q150 104 0 40Z" fill="#fff"/></svg>
    <span class="brand-dot" style="left:24px; top:3px; width:40px; height:40px;"></span>
    <span class="t brand-name" style="left:84px; top:1px; font-size:22px;">Fundlark</span>
    <span class="t brand-line" style="left:73px; top:31px; font-size:13px;">Project + Crowd = FUNDING</span>
    <span class="t t-center headline" style="top:77px; font-size:22px;">FREE</span>
    <span class="t t-center headline" style="top:110px; font-size:22px;">CROWDFUNDING</span>
    <span class="t t-center headline" style="top:136px; font-size:22px;">CONSULTATION</span>
    <span class="t t-center" style="top:178px; font-size:13px;">IS YOUR PROJECT VIABLE</span>
    <a class="cta">Learn More <svg viewBox="0 0 18 18"><circle cx="9" cy="9" r="9" fill="#fff"/><polygon points="7,5 13,9 7,13" fill="var(--cta-arrow)"/></svg></a>
  </section>

  <section class="banner rectangle" style="left:438px;">
    <div class="banner-art" role="img" aria-label="Blue sky gradient backdrop"
         style="background:linear-gradient(var(--sky-top) 0%, var(--sky-mid) 45%, var(--sky-low) 75%, #1d3474 100%);"></div>
    <svg class="banner-art" viewBox="0 0 300 250" aria-hidden="true"><path d="M0 0H300V40Q150 104 0 40Z" fill="#fff"/></svg>
    <span class="brand-dot" style="left:24px; top:3px; width:40px; height:40px;"></span>
    <span class="t brand-name" style="left:84px; top:1px; font-size:22px;">Fundlark</span>
    <span class="t brand-line" style="left:73px; top:31px; font-size:13px;">Project + Crowd = FUNDING</span>
    <span class="t t-center headline" style="top:77px; font-size:22px;">FREE</span>
    <span class="t t-center headline" style="top:110px; font-size:22px;">CROWDFUNDING</span>
    <span class="t t-center headline" style="top:136px; font-size:22px;">CONSULTATION</span>
    <span class="t t-center" style="top:178px; font-size:13px;">IS YOUR PROJECT VIABLE</span>
    <a class="cta">Learn More <svg viewBox="0 0 18 18"><circle cx="9" cy="9" r="9" fill="#fff"/><polygon points="7,5 13,9 7,13" fill="var(--cta-arrow)"/></svg></a>
  </section>

  <!-- Skyscrapers -->
  <section class="banner skyscraper" style="left:812px;">
    <div class="banner-art" role="img" aria-label="Deep navy and violet faceted backdrop"
         style="background:linear-gradient(170deg, var(--navy-deep) 25%, var(--navy-mid) 55%, var(--violet) 75%, var(--violet-glow) 100%);"></div>
    <svg class="banner-art" viewBox="0 0 160 600" aria-hidden="true">
      <polygon fill="#fff" points="0,0 160,0 160,156 154,163 148,156 142,163 136,156 130,163 124,156 118,163 112,156 106,163 100,156 94,163 88,156 82,163 76,156 70,163 64,156 58,163 52,156 46,163 40,156 34,163 28,156 22,163 16,156 10,163 4,156 0,160"/>
    </svg>
    <span class="brand-dot" style="left:51px; top:8px; width:60px; height:60px;"></span>
    <span class="t t-center brand-name" style="top:66px; font-size:22px;">Fundlark</span>
    <span class="t t-center brand-line" style="top:96px; font-size:14px;">Project + Crowd</span>
    <span class="t t-center brand-line" style="top:110px; font-size:14px;">=</span>
    <span class="t t-center brand-line" style="top:125px; font-size:14px;">Funding</span>
    <span class="t t-center" style="top:225px; font-size:21px;">GET YOUR</span>
    <span class="t headline accent" style="left:12px; top:285px; font-size:34px;">FREE</span>
    <span class="t headline accent" style="right:12px; top:327px; font-size:30px;">GUIDE</span>
    <span class="t t-center headline" style="top:413px; font-size:22px;">SUCCESSFUL</span>
    <span class="t t-center" style="top:440px; font-size:17px;">CROWDFUNDING</span>
    <div class="base-band"></div>
    <a class="cta">LEARN MORE <svg viewBox="0 0 18 18"><circle cx="9" cy="9" r="9" fill="#fff"/><polygon points="7,5 13,9 7,13" fill="var(--cta-arrow)"/></svg></a>
  </section>

  <section class="banner skyscraper" style="left:993px;">
    <div class="banner-art" role="img" aria-label="Plum and magenta faceted backdrop"
         style="background:linear-gradient(160deg, var(--plum-glow) 15%, var(--plum-mid) 50%, var(--plum-deep) 100%);"></div>
    <svg class="banner-art" viewBox="0 0 160 600" aria-hidden="true">
      <polygon fill="#fff" points="0,0 160,0 160,156 154,163 148,156 142,163 136,156 130,163 124,156 118,163 112,156 106,163 100,156 94,163 88,156 82,163 76,156 70,163 64,156 58,163 52,156 46,163 40,156 34,163 28,156 22,163 16,156 10,163 4,156 0,160"/>
    </svg>
    <span class="brand-dot" style="left:51px; top:8px; width:60px; height:60px;"></span>
    <span class="t t-center brand-name" style="top:66px; font-size:22px;">Fundlark</span>
    <span class="t t-center brand-line" style="top:96px; font-size:14px;">Project + Crowd</span>
    <span class="t t-center brand-line" style="top:110px; font-size:14px;">=</span>
    <span class="t t-center brand-line" style="top:125px; font-size:14px;">Funding</span>
    <span class="t t-center" style="top:225px; font-size:21px;">GET YOUR</span>
    <span class="t headline accent" style="left:12px; top:285px; font-size:34px;">FREE</span>
    <span class="t headline accent" style="right:12px; top:327px; font-size:30px;">GUIDE</span>
    <span class="t t-center headline" style="top:413px; font-size:22px;">SUCCESSFUL</span>
    <span class="t t-center" style="top:440px; font-size:17px;">CROWDFUNDING</span>
    <div class="base-band"></div>
    <a class="cta">LEARN MORE <svg viewBox="0 0 18 18"><circle cx="9" cy="9" r="9" fill="#fff"/><polygon points="7,5 13,9 7,13" fill="var(--cta-arrow)"/></svg></a>
  </section>

  <!-- Small squares -->
  <section class="banner square" style="left:560px; top:700px;">
    <div class="banner-art" role="img" aria-label="Deep navy and violet faceted backdrop"
         style="background:linear-gradient(135deg, var(--navy-deep) 15%, var(--navy-mid) 55%, var(--violet-glow) 100%);"></div>
    <span class="t accent" style="left:5px; top:3px; font-size:15px;">GET YOUR</span>
    <span class="t accent" style="left:5px; top:23px; font-size:15px;">FREE GUIDE TO</span>
    <span class="t headline" style="left:11px; top:54px; font-size:19px;">SUCCESSFUL</span>
    <span class="t headline" style="left:11px; top:78px; font-size:19px;">CROWDFUNDIN</span>
    <a class="cta">Learn More <svg viewBox="0 0 18 18"><circle cx="9" cy="9" r="9" fill="#fff"/><polygon points="7,5 13,9 7,13" fill="var(--cta-arrow)"/></svg></a>
  </section>

  <section class="banner square" style="left:807px; top:697px;">
    <div class="banner-art" role="img" aria-label="Plum and magenta faceted backdrop"
         style="background:linear-gradient(135deg, var(--plum-mid) 10%, var(--plum-glow) 60%, var(--plum-mid) 100%);"></div>
    <span class="t accent" style="left:5px; top:3px; font-size:15px;">GET YOUR</span>
    <span class="t accent" style="left:5px; top:23px; font-size:15px;">FREE GUIDE TO</span>
    <span class="t headline" style="left:11px; top:54px; font-size:19px;">SUCCESSFUL</span>
    <span class="t headline" style="left:11px; top:78px; font-size:19px;">CROWDFUNDIN</span>
    <a class="cta">Learn More <svg viewBox="0 0 18 18"><circle cx="9" cy="9" r="9" fill="#fff"/><polygon points="7,5 13,9 7,13" fill="var(--cta-arrow)"/></svg></a>
  </section>
</body>
</html>
```